Domain Search Page and Results

We are looking for creative methods to display a domain registration search page, with many extensions. We are only looking for designs of the inside of the page and not for the frame around the page.
There are currently 4 categories and after pressing submit there is the results: however in the future there will be more categories (around 7 or 8) and domain extensions.
We would like creative methods to display the different (7-8) categories and extensions and also the results display.
The categories should be open/close-able.
We are planning to use JQuery and your suggestions for any movement will be appreciated.
We also would like creative ways to display the results.
Thank you.
Additions:
- It is not necessary to change the template/frame of the page. We are only looking for the search AND results display.
- We are looking for creative ideas and not necessary judging based on the actual design.
- We are basing the winner on how creatively it will be possible to display the search function AND results display. And to display creatively 7 or 8 categories with 100''s of domain extensions. The more creative and yet still user friendly the search functionality is, the chances of being selected will be higher.
- There will be 7 or 8 categories (and not just 4 as in the sample). The design must be able to extend to 7 or 8 categories. In some categories there are over 100 extensions. Creative ideas on how to sub categorize the extensions will be a bonus.

```html
<!DOCTYPE html>
<html lang="en">
<head>
<meta charset="utf-8">
<title>Domain Search Availability</title>
<link href="https://fonts.googleapis.com/css2?family=Open+Sans:wght@400;600;700&display=swap" rel="stylesheet">
<style>
:root{
  --red:#d8232a;
  --dark:#3a3a3a;
  --darker:#2b2b2b;
  --grey:#f1f1f1;
  --line:#d9d9d9;
  --text:#555;
  --muted:#888;
  --ok:#3d8a3d;
  --bg:#ffffff;
}
*{box-sizing:border-box;margin:0;padding:0}
html,body{width:900px;height:1200px;overflow:hidden;background:var(--bg);font-family:"Open Sans",Arial,sans-serif;color:var(--text)}
.page{position:relative;width:900px;height:1200px}
.wrap{position:absolute;left:90px;width:720px}
.brand{top:22px;height:56px;display:flex;align-items:center}
.brand-name{font-size:26px;font-weight:700;color:var(--darker);white-space:nowrap}
.account{position:absolute;right:90px;top:40px;font-size:11px;color:var(--text);display:flex;align-items:center;gap:12px;white-space:nowrap}
.account a{color:var(--red);text-decoration:none;font-weight:600}
.lang{border:1px solid var(--line);padding:3px 8px;display:flex;align-items:center;gap:6px;font-size:10px}
.flag{width:16px;height:11px;background:#4a5fa0}
.nav{top:90px;height:34px;background:var(--dark);display:flex;font-size:11px;font-weight:600;color:#fff;white-space:nowrap}
.nav span{padding:0 14px;line-height:34px}
.nav .cp{margin-left:auto;background:var(--red);padding:0 20px}
.crumb{top:128px;height:24px;background:var(--grey);font-size:10px;line-height:24px;padding-left:12px;color:var(--muted)}
.title{top:164px;font-size:22px;line-height:30px;color:var(--red);font-weight:400}
.intro{top:200px;font-size:10.5px;line-height:15px}
.intro a,.hint{color:var(--red)}
.entry{top:284px;height:160px;border:1px solid var(--line);padding:12px 14px}
.entry label{font-size:10.5px}
.entry .box{margin-top:8px;height:108px;border:1px solid var(--line)}
.acc{left:90px;width:720px;position:absolute;border:1px solid var(--line)}
.acc-head{height:44px;display:flex;align-items:center;justify-content:space-between;padding:0 14px;font-size:13px;color:var(--darker)}
.acc-open .acc-head{color:var(--red);border-bottom:1px solid var(--line)}
.ext{display:grid;grid-template-columns:repeat(4,90px);row-gap:8px;padding:10px 18px;font-size:10.5px}
.ext span{display:flex;align-items:center;gap:6px;white-space:nowrap}
.cb{width:10px;height:10px;border:1px solid #999;display:inline-block}
.btn{position:absolute;height:28px;padding:0 20px;line-height:28px;font-size:11px;font-weight:600;color:#fff;white-space:nowrap}
.search{left:90px;top:804px;background:var(--red)}
.results{top:842px;height:222px;border:1px solid var(--line);padding:8px 14px 10px}
.res-head{display:flex;justify-content:space-between;align-items:center;margin-bottom:6px}
.res-head h2{font-size:14px;color:var(--red);font-weight:400}
.res-head small{font-size:10px}
.res-head small a{color:var(--red)}
table{width:100%;border-collapse:collapse;font-size:10.5px}
th{background:var(--dark);color:#fff;font-weight:600;text-align:left;padding:5px 10px}
td{padding:5px 10px;border-bottom:1px solid var(--line)}
.ok{color:var(--ok)}.unk{color:var(--red)}
.purchase{left:90px;top:1090px;background:var(--darker)}
.footer{position:absolute;left:0;top:1134px;width:900px;height:66px;background:var(--darker);color:#bbb;font-size:10px;text-align:center;padding-top:16px;line-height:18px}
</style>
</head>
<body>
<div class="page">
  <div class="wrap brand"><div class="brand-name">Kumo Names</div></div>
  <div class="account"><span><a>LOGIN HERE</a> / <a>CREATE A NEW ACCOUNT</a></span><span class="lang"><span class="flag"></span>ENGLISH ▾</span></div>

  <nav class="wrap nav"><span>HOME</span><span>PRICING</span><span>SEARCH</span><span>FAQ</span><span>HOSTING IN JAPAN</span><span>RESELLERS</span><span>CONTACT US</span><span class="cp">CONTROL PANEL</span></nav>
  <div class="wrap crumb">JP Domains</div>

  <h1 class="wrap title">Domain Search Availability</h1>
  <p class="wrap intro">To search for multiple domains, please enter the domains in the textarea below.<br>
  If the domain is available, you may continue to register the domain. If the domain is unavailable, please search<br>
  for an alternate domain.<br>
  <span class="hint">Hint:</span> Make sure to check your company domain isn't already taken. Enter the domain below and press<br>
  <a>"Search Here"</a>.</p>

  <div class="wrap entry"><label>Enter domain(s) below:</label><div class="box"></div></div>

  <section class="acc acc-open" style="top:500px;height:92px">
    <div class="acc-head">Japan Domains<svg width="16" height="16"><circle cx="8" cy="8" r="7" fill="#555"/><rect x="4" y="7" width="8" height="2" fill="#fff"/></svg></div>
    <div class="ext">
      <span><i class="cb"></i>.jp</span><span><i class="cb"></i>.ne.jp</span><span><i class="cb"></i>.co.jp</span><span><i class="cb"></i>.gr.jp</span>
      <span><i class="cb"></i>.hokkaido.jp</span><span><i class="cb"></i>.osaka.jp</span><span><i class="cb"></i>.kyoto.jp</span>
    </div>
  </section>
  <section class="acc" style="top:630px"><div class="acc-head">Japan Regional Domains<svg width="16" height="16"><circle cx="8" cy="8" r="7" fill="#555"/><rect x="4" y="7" width="8" height="2" fill="#fff"/><rect x="7" y="4" width="2" height="8" fill="#fff"/></svg></div></section>
  <section class="acc" style="top:682px"><div class="acc-head">gTLD Domains<svg width="16" height="16"><circle cx="8" cy="8" r="7" fill="#555"/><rect x="4" y="7" width="8" height="2" fill="#fff"/><rect x="7" y="4" width="2" height="8" fill="#fff"/></svg></div></section>
  <section class="acc" style="top:734px"><div class="acc-head">ccTLD Domains<svg width="16" height="16"><circle cx="8" cy="8" r="7" fill="#555"/><rect x="4" y="7" width="8" height="2" fill="#fff"/><rect x="7" y="4" width="2" height="8" fill="#fff"/></svg></div></section>

  <div class="btn search">SEARCH</div>

  <section class="wrap results">
    <div class="res-head"><h2>Results</h2><small>Results shown here after pressing <a>Search</a></small></div>
    <table>
      <tr><th>Domain Name</th><th style="width:150px">Results</th><th style="width:90px">Check</th></tr>
      <tr><td>mysampleword.jp</td><td class="ok">Available</td><td><i class="cb"></i></td></tr>
      <tr><td>mysampleword.com</td><td class="ok">Available</td><td><i class="cb"></i></td></tr>
      <tr><td>mysampleword.net</td><td class="ok">Available</td><td><i class="cb"></i></td></tr>
      <tr><td>mysampleword.org</td><td class="unk">Unknown</td><td><i class="cb"></i></td></tr>
      <tr><td>mysampleword.club</td><td class="ok">Available</td><td><i class="cb"></i></td></tr>
      <tr><td>mysampleword.in</td><td class="ok">Available</td><td><i class="cb"></i></td></tr>
    </table>
  </section>

  <div class="btn purchase">DOMAIN PURCHASE</div>

  <footer class="footer">Login &nbsp;|&nbsp; Translations &nbsp;|&nbsp; Privacy Policy &nbsp;|&nbsp; TOS &nbsp;|&nbsp; About Us<br>Copyright © 2010–2014 kumonames.example. All rights reserved.</footer>
</div>
</body>
</html>
```